Book cover for book of Poems "Lanternfall"

I have written a book of poems. The book is titled "Lanternfall" and has 160 pages. The poems were written mostly during my youth but there are newer poems also written over the past 10 years (I'm 42 now). They are mostly about love, loss, social conformity, and nature. I'm influenced a lot by the English Romantic Poets, gothic motives, and 80s music by bands such as The Vell, Porvana & the Quillets, and Tabberley. I need an original book cover design for my book. Attached are samples of designs I like and few of my poems. The cover will be a hardcover and I need design for Front Cover, Back Cover, and Spine. Dimension is 6"x9". Front Cover should have name of book "Lanternfall" and name of author "Ravi Dunsker". Thanks.
Updates

Further details which I should have included in my original brief -The book cover will be a hard cover. Design is required for front cover, back cover, and spine. Dimension is 6x9.Front should have book title "Lanternfall" and author's name "Ravi Dunsker". Added Monday, December 19, 2016

Target Market(s)

Mostly friends and family

Requirements
Must have
• I don't mind a design where lanternfall is spelled out in big capital letters and text from one of my poems is inside, like the sample I've attached.

```html
<!DOCTYPE html>
<html lang="en">
<head>
<meta charset="utf-8">
<title>Lanternfall — Cover Spread</title>
<link href="https://fonts.googleapis.com/css2?family=Grenze:wght@700&family=Cinzel+Decorative:wght@700&family=Cinzel:wght@600;700&family=Alegreya+Sans:ital,wght@1,800&display=swap" rel="stylesheet">
<style>
  :root {
    --backdrop: #e8ebdd;
    --ink: #141414;
    --title-ink: #232323;
    --silver: #c4c4c4;
    --poem-grey: rgba(72, 72, 72, 0.8);
    --spiral-grey: rgba(95, 95, 95, 0.75);
    --blurb: #f6f6f6;
  }
  * { margin: 0; padding: 0; box-sizing: border-box; }
  html, body { width: 1200px; height: 900px; overflow: hidden; background: var(--backdrop); }

  .spread {
    position: absolute; left: 113px; top: 113px; width: 975px; height: 675px;
    overflow: hidden; box-shadow: 0 2px 6px rgba(0,0,0,0.35);
  }
  .forest-photo {
    position: absolute; inset: 0;
    background:
      radial-gradient(ellipse 170px 150px at 560px 380px, rgba(255,255,255,0.9), rgba(255,255,255,0) 75%),
      radial-gradient(ellipse 420px 330px at 760px 140px, rgba(248,250,248,0.95), rgba(248,250,248,0) 80%),
      radial-gradient(ellipse 260px 260px at 470px 140px, rgba(240,243,240,0.8), rgba(240,243,240,0) 80%),
      linear-gradient(180deg, rgba(255,255,255,0) 0%, rgba(255,255,255,0) 70%, rgba(95,100,80,0.55) 100%),
      linear-gradient(90deg, #5f635c 0%, #8c918a 18%, #aeb3ac 40%, #d4d8d3 60%, #c9ccc7 80%, #b0b4ae 100%);
  }
  .spread-art { position: absolute; left: 0; top: 0; width: 975px; height: 675px; }

  .title-text { font-family: "Grenze", serif; font-weight: 700; fill: var(--title-ink); text-transform: uppercase; }
  .author-text { font-family: "Cinzel", serif; font-weight: 700; text-transform: uppercase; }
  .author-text--dark { fill: var(--ink); }
  .author-text--silver { fill: var(--silver); }
  .spiral-text { font-family: "Alegreya Sans", sans-serif; font-style: italic; font-weight: 800; font-size: 14px; fill: var(--spiral-grey); }

  .back-blurb {
    position: absolute; left: 71px; top: 211px; width: 330px; text-align: center;
    font-family: "Cinzel", serif; font-weight: 600; font-size: 7.4px; line-height: 11px;
    color: var(--blurb); text-shadow: 0 0 2px rgba(0,0,0,0.45); white-space: nowrap;
  }
  .back-blurb p + p { margin-top: 11px; }

  .contents {
    position: absolute; left: 65px; top: 335px; display: flex;
    font-family: "Cinzel", serif; font-weight: 600; font-size: 7.4px; line-height: 10.9px;
    color: var(--blurb); text-shadow: 0 0 2px rgba(0,0,0,0.45); white-space: nowrap;
  }
  .contents ul { list-style: none; }
  .contents ul:nth-child(1) { width: 116px; }
  .contents ul:nth-child(2) { width: 110px; }

  .poem-excerpt {
    position: absolute; left: 592px; top: 322px; width: 300px;
    font-family: "Alegreya Sans", sans-serif; font-style: italic; font-weight: 800;
    font-size: 14px; line-height: 18px; color: var(--poem-grey); white-space: nowrap;
    transform: rotate(-9deg); transform-origin: 0 0;
  }
  .poem-excerpt span { display: block; }

  .figure-silhouette {
    position: absolute; left: 760px; top: 319px; width: 215px; height: 300px;
    background: #0b0b0b; border-radius: 90px 90px 0 0;
  }
</style>
</head>
<body>
  <main class="spread">
    <div class="forest-photo" role="img" aria-label="Photograph of a misty pine forest with sunlight breaking through the tall trunks"></div>

    <svg class="spread-art" viewBox="0 0 975 675" aria-hidden="true">
      <defs>
        <path id="spiral-path" d="M520 30 C 610 50, 620 330, 520 355 C 430 370, 415 130, 500 125 C 565 120, 570 290, 505 295"/>
      </defs>
      <text class="spiral-text"><textPath href="#spiral-path">we've turned into the sun and moon and moon we've turned into the sun and moon to fall on</textPath></text>
    </svg>

    <div class="back-blurb">
      <p>These poems were written mostly during my youth, but there are<br>newer poems also written over the past 10 years.</p>
      <p>They are mostly about love, loss, social conformity, and nature.</p>
      <p>I'm influenced a lot by the English Romantic Poets, gothic motives,<br>and 80s music by bands such as<br>The Vell, Porvana &amp; the Quillets, and Tabberley.</p>
    </div>
    <div class="contents">
      <ul><li>Once</li><li>Jealous</li><li>Sometimes I Wonder</li><li>One Look</li><li>The User, the Used</li><li>One Sighted Love</li><li>Better…</li><li>Ode to Delight</li></ul>
      <ul><li>Love Song</li><li>The Cloud, the Mist</li><li>Why</li><li>Ode to Sound</li><li>On Life</li><li>Look</li><li>To you Stars</li><li>My Land</li></ul>
      <ul><li>Adventure</li><li>To my Parents</li><li>Tonight</li><li>These are the days</li><li>God too cries</li><li>Sounds and Words</li><li>Traveller</li><li>… and so much more</li></ul>
    </div>

    <p class="poem-excerpt">
      <span>We've turned into night and day</span>
      <span>When one is alit</span>
      <span>The other's in dismay</span>
      <span>We've turned into night and day</span>
      <span>Were we never meant for love</span>
      <span>Is love not for you and I</span>
      <span>Love never welcomed us</span>
      <span>Did you just skip us by?</span>
    </p>

    <div class="figure-silhouette" role="img" aria-label="Dark silhouette of a seated figure with long hair"></div>

    <svg class="spread-art" viewBox="0 0 975 675">
      <defs>
        <filter id="author-glow" x="-20%" y="-60%" width="140%" height="220%">
          <feDropShadow dx="0" dy="0" stdDeviation="6" flood-color="#000" flood-opacity="0.95"/>
        </filter>
      </defs>
      <path d="M0 607 C 250 600, 560 610, 760 619 L 975 619 L 975 675 L 0 675 Z" fill="var(--ink)"/>

      <text class="title-text" x="91" y="191" font-size="100" textLength="298" lengthAdjust="spacingAndGlyphs">Lanternfall</text>
      <text class="author-text author-text--dark" x="135" y="477" font-size="36" textLength="198" lengthAdjust="spacingAndGlyphs">Ravi Dunsker</text>

      <text class="title-text" transform="translate(471 33) rotate(90)" font-size="50" textLength="354" lengthAdjust="spacingAndGlyphs">Lanternfall</text>
      <text class="author-text author-text--dark" transform="translate(475 395) rotate(90)" font-size="27" textLength="168" lengthAdjust="spacingAndGlyphs">Ravi Dunsker</text>

      <text class="title-text" x="563" y="259" font-size="220" textLength="370" lengthAdjust="spacingAndGlyphs">Lanternfall</text>
      <text class="author-text author-text--silver" x="615" y="619" font-size="41" textLength="266" lengthAdjust="spacingAndGlyphs" filter="url(#author-glow)">Ravi Dunsker</text>
    </svg>
  </main>
</body>
</html>
```